VELMORHAVEN

We just changed our name from Quillhacks to Velmorrhaven so we need a new website. have been in the catering &special events business for 36 years . We are an in house caterer with homemade food and best around our name has always hurt us so we changed it and want a new web site to go with it. The current website Quillhacks banquet center .com can be viewed but, is horrible. I have been to many website companies in the past years and have never had a profesinal website. What brides want to see on the web are pictures and I feel they do not necessarily have to be from this facility they can be stock photos that resemble this place.

weddings partys

Business

5+ page

Must have
• pictures
Nice to have
• we have done functions for the king of Jordan on his plane and other famous people including celebrities and stars. This was when we were doing airline catering years ago, but, does not matter if plane or our facility they do not need to know that. Their were many people who have come to us from all over the world for private functions. Consider the possibilities memorable Weddings, exciting anniversaries and birthday parties .

```html
<!DOCTYPE html>
<html lang="en">
<head>
<meta charset="utf-8">
<title>Velmorhaven — Your Event Hire Specialists</title>
<link rel="stylesheet" href="https://fonts.googleapis.com/css2?family=Libre+Baskerville:wght@400;700&family=Lato:wght@400;700&family=Exo+2:wght@700&display=swap">
<style>
:root{
  --page:#efefef;
  --white:#ffffff;
  --maroon:#9a3d5a;
  --maroon-dark:#7e2f48;
  --rose-text:#a4506b;
  --body-text:#8a8585;
  --nav-text:#3a3434;
  --nav-num:#b06a80;
  --teal:#7fb3b0;
  --footer:#231f20;
  --footer-text:#d9d4d4;
  --footer-link:#7fc0c9;
  --orange:#d97a1f;
}
*{margin:0;padding:0;box-sizing:border-box}
html,body{width:1200px;height:3377px;overflow:hidden}
body{position:relative;background:var(--page);font-family:"Lato",sans-serif;color:var(--body-text)}
.abs{position:absolute}

/* top bar */
.topbar{left:0;top:0;width:1200px;height:46px;background:var(--white)}
.topbar-rule{left:115px;top:40px;width:966px;height:4px;background:#e9e9e9}
.phone{right:120px;top:4px;font-family:"Libre Baskerville",serif;font-size:19px;color:var(--nav-text);display:flex;align-items:center;gap:10px}
.phone-icon{width:22px;height:22px;background:var(--maroon);border-radius:3px;display:flex;align-items:center;justify-content:center}

/* floral backdrop */
.backdrop{left:0;top:46px;width:1200px;height:1902px;
  background:
   radial-gradient(ellipse 260px 340px at 60px 1100px, rgba(232,150,160,.55), transparent),
   radial-gradient(ellipse 280px 360px at 1150px 1050px, rgba(236,160,165,.6), transparent),
   radial-gradient(ellipse 300px 300px at 1120px 1750px, rgba(225,140,150,.45), transparent),
   radial-gradient(ellipse 240px 300px at 40px 1750px, rgba(240,200,190,.6), transparent),
   radial-gradient(ellipse 300px 260px at 1100px 500px, rgba(245,190,185,.55), transparent),
   linear-gradient(180deg,#f2efed 0%,#f1dcd6 20%,#efe2dc 50%,#efd6d2 75%,#f0f0f0 100%)}

/* nav */
.nav{left:115px;top:60px;display:flex;gap:30px;font-family:"Libre Baskerville",serif;font-size:15px;color:var(--nav-text);letter-spacing:.3px}
.nav span.num{color:var(--nav-num);margin-right:4px}
.socials{left:940px;top:60px;display:flex;gap:12px}
.socials i{display:block;width:25px;height:25px;border:2px solid #c9c9c9;border-radius:50%}

/* logo band + hero */
.brand-band{left:115px;top:104px;width:966px;height:122px;background:var(--maroon);text-align:center;color:var(--white)}
.brand-name{margin-top:28px;font-family:"Libre Baskerville",serif;font-size:43px;letter-spacing:1px}
.brand-tag{font-size:11px;letter-spacing:1.2px;margin-top:2px}
.hero{left:115px;top:226px;width:966px;height:374px;
  background:linear-gradient(115deg,#3a2a2c 0%,#c27a9a 18%,#f0d6e6 30%,#c98aa8 40%,#d97a1f 45.5%,#e8a04a 47%,#2a1e14 48.5%,#6a4a22 58%,#e0b060 70%,#3a2816 85%,#c7904a 100%)}
.hero-caption{left:115px;top:484px;width:320px;height:70px;background:rgba(200,104,30,.85);color:var(--white);font-family:"Libre Baskerville",serif;font-weight:700;font-size:17px;line-height:22px;padding:10px 18px;letter-spacing:.5px}

/* event cards */
.card{left:115px;width:966px;height:298px;background:rgba(255,255,255,.78)}
.card .photo{position:absolute;top:5px;width:458px;height:288px}
.card .photo.left{left:7px}
.card .photo.right{right:7px}
.arrow{position:absolute;top:50%;margin-top:-10px;width:20px;height:20px}
.arrow.prev{left:10px}
.arrow.next{right:10px}
.card .copy{position:absolute;top:38px;width:440px}
.card .copy.right{left:491px}
.card .copy.left{left:46px}
.card h2{font-family:"Libre Baskerville",serif;font-weight:400;font-size:18px;color:var(--rose-text);letter-spacing:1px;margin-bottom:14px}
.card p{font-size:13.5px;line-height:23px;color:var(--body-text)}
.btn{display:inline-block;margin-top:24px;background:var(--maroon);color:var(--white);font-size:13px;padding:6px 22px;border-radius:6px}

.photo-wedding{background:linear-gradient(160deg,#e6c6e8,#b07ac6 45%,#7a4a8a 75%,#d9c3de)}
.photo-anniv{background:linear-gradient(180deg,#d8bff0,#a882d6 50%,#3e2c5a 85%,#1e1530)}
.photo-bar{background:linear-gradient(135deg,#2a1616,#b81e26 40%,#5a1a1a 65%,#e8e2e0 90%)}
.photo-sweet{background:linear-gradient(160deg,#0b1a3a,#1f6ec4 35%,#36c4c0 55%,#d83a9a 75%,#1a1a3a)}

/* video */
.video{left:115px;top:1982px;width:966px;height:396px;background:#0a0a0a}
.video-still{left:245px;top:1982px;width:706px;height:396px;background:linear-gradient(180deg,#8a6e52,#d9b98a 30%,#bfa07a 55%,#e6d3c0 80%,#8a7360)}
.video-title{left:245px;top:2000px;width:706px;text-align:center;color:rgba(255,255,255,.92);font-family:"Libre Baskerville",serif;font-size:36px;line-height:46px;letter-spacing:1px}
.video-tools{left:1046px;top:1993px;display:flex;flex-direction:column;gap:12px}
.video-bar{left:115px;top:2340px;width:966px;height:38px;background:rgba(0,0,0,.55);display:flex;align-items:center;padding:0 16px;gap:14px}
.track{flex:1;height:8px;background:#444}
.hd{color:#fff;font-size:13px;font-weight:700}

/* gallery */
.gallery{left:115px;top:2436px;width:966px;height:442px;background:var(--white);border-top:5px solid var(--teal)}
.gallery h2{position:absolute;left:34px;top:34px;font-family:"Libre Baskerville",serif;font-weight:400;font-size:28px;color:#5a9a9a;letter-spacing:1px}
.gallery-rule{position:absolute;left:20px;right:20px;top:100px;height:2px;background:#eeeeee}
.gallery-shadow{left:115px;top:2880px;width:966px;height:8px;background:linear-gradient(90deg,#bdbdbd,transparent 30%,transparent 70%,#bdbdbd)}
.thumb{top:2577px;height:258px}
.g-arrow{top:2680px;font-size:30px;color:#333}

.thumb-1{left:167px;width:280px;background:linear-gradient(140deg,#2a1a0a,#c89a3a 40%,#f2e0a0 55%,#2a4a1a 80%)}
.thumb-2{left:457px;width:282px;background:linear-gradient(160deg,#6a5a4a,#e8c890 40%,#f0d8b0 60%,#8a6a4a)}
.thumb-3{left:747px;width:282px;background:linear-gradient(180deg,#c84a3a,#e8e0d8 35%,#b01420 60%,#f2ecec 90%)}

/* footer */
.footer{left:0;top:2954px;width:1200px;height:374px;background:var(--footer);color:var(--footer-text)}
.footer h3{font-family:"Exo 2",sans-serif;font-weight:700;font-size:19px;color:var(--white);margin-bottom:14px;letter-spacing:.5px}
.fcol{position:absolute;top:50px;font-size:11.5px;line-height:18px}
.fcol.about{left:115px;width:330px}
.fcol.address{left:480px;width:220px}
.fcol.quotes{left:745px;width:340px}
.footer a{color:var(--footer-link);text-decoration:none}
.quote{display:flex;gap:18px;margin-bottom:28px}
.avatar{width:50px;height:50px;flex:none;background:#8a8080;margin-top:4px}
.quote em{display:block;font-style:normal;font-weight:700;color:#8fd06a;font-size:10.5px}
.copyright{left:0;top:3328px;width:1200px;height:49px;background:var(--maroon-dark);color:#f0dde3;font-size:12px;text-align:center;line-height:49px}
</style>
</head>
<body>

<div class="abs topbar"></div>
<div class="abs topbar-rule"></div>
<div class="abs phone">
  <span class="phone-icon"><svg width="12" height="12" viewBox="0 0 24 24"><path fill="#fff" d="M6.6 10.8a15 15 0 0 0 6.6 6.6l2.2-2.2c.3-.3.7-.4 1-.2 1.1.4 2.3.6 3.6.6.6 0 1 .4 1 1V20c0 .6-.4 1-1 1A17 17 0 0 1 3 4c0-.6.4-1 1-1h3.5c.6 0 1 .4 1 1 0 1.3.2 2.5.6 3.6.1.3 0 .7-.2 1z"/></svg></span>
  Phone: (555) 410-2286
</div>

<div class="abs backdrop" role="img" aria-label="Soft blurred backdrop of pink and peach wedding flowers"></div>

<nav class="abs nav">
  <span><span class="num">01.</span>HOME</span>
  <span><span class="num">02.</span>SERVICES</span>
  <span><span class="num">03.</span>GALLERY</span>
  <span><span class="num">04.</span>CONTACT US</span>
</nav>
<div class="abs socials"><i></i><i></i><i></i><i></i></div>

<header class="abs brand-band">
  <div class="brand-name">VELMORHAVEN</div>
  <div class="brand-tag">YOUR EVENT HIRE SPECIALISTS</div>
</header>
<div class="abs hero" role="img" aria-label="Two wedding photos split diagonally: a pink draped ceremony stage and a candlelit banquet hall"></div>
<div class="abs hero-caption">THE PERFECT WEDDING<br>EXPERIENCE</div>

<section class="abs card" style="top:653px">
  <div class="photo left photo-wedding" role="img" aria-label="Wedding reception hall with white chairs and purple lighting">
    <svg class="arrow prev" viewBox="0 0 20 20"><path d="M13 4 6 10l7 6z" fill="#fff"/></svg>
    <svg class="arrow next" viewBox="0 0 20 20"><path d="M7 4l7 6-7 6z" fill="#fff"/></svg>
  </div>
  <div class="copy right">
    <h2>WEDDING PICTURES</h2>
    <p>Lorem Ipsum has been the industry's standard dummy text ever since the 1500s, when an unknown printer took a galley of type and scrambled it to make a type specimen book. It has survived not only five centuries, but also the leap into electronic typesetting, remaining essentially unchanged.</p>
    <span class="btn">Read More</span>
  </div>
</section>

<section class="abs card" style="top:973px">
  <div class="copy left">
    <h2>ANNIVERSARY PICTURES</h2>
    <p>Lorem Ipsum has been the industry's standard dummy text ever since the 1500s, when an unknown printer took a galley of type and scrambled it to make a type specimen book. It has survived not only five centuries, but also the leap into electronic typesetting, remaining essentially unchanged.</p>
    <span class="btn">Read More</span>
  </div>
  <div class="photo right photo-anniv" role="img" aria-label="Anniversary party with a ceiling of lilac balloons above guests">
    <svg class="arrow prev" viewBox="0 0 20 20"><path d="M13 4 6 10l7 6z" fill="#fff"/></svg>
    <svg class="arrow next" viewBox="0 0 20 20"><path d="M7 4l7 6-7 6z" fill="#fff"/></svg>
  </div>
</section>

<section class="abs card" style="top:1295px">
  <div class="photo left photo-bar" role="img" aria-label="Bar mitzvah party set with red racing car and checkered flags">
    <svg class="arrow prev" viewBox="0 0 20 20"><path d="M13 4 6 10l7 6z" fill="#fff"/></svg>
  </div>
  <div class="copy right">
    <h2>BAR / BAZMIT &nbsp;PICTURES</h2>
    <p>Lorem Ipsum has been the industry's standard dummy text ever since the 1500s, when an unknown printer took a galley of type and scrambled it to make a type specimen book. It has survived not only five centuries, but also the leap into electronic typesetting, remaining essentially unchanged.</p>
    <span class="btn">Read More</span>
  </div>
</section>

<section class="abs card" style="top:1614px">
  <div class="copy left">
    <h2>SWEET SIXTEEN PICTURES</h2>
    <p>Lorem Ipsum has been the industry's standard dummy text ever since the 1500s, when an unknown printer took a galley of type and scrambled it to make a type specimen book. It has survived not only five centuries, but also the leap into electronic typesetting, remaining essentially unchanged.</p>
    <span class="btn">Read More</span>
  </div>
  <div class="photo right photo-sweet" role="img" aria-label="Sweet sixteen party with tables glowing in blue, green and pink light">
    <svg class="arrow prev" viewBox="0 0 20 20"><path d="M13 4 6 10l7 6z" fill="#fff"/></svg>
    <svg class="arrow next" viewBox="0 0 20 20"><path d="M7 4l7 6-7 6z" fill="#fff"/></svg>
  </div>
</section>

<div class="abs video"></div>
<div class="abs video-still" role="img" aria-label="Video still of an elegant banquet hall with chandeliers and set tables"></div>
<div class="abs video-title">INSPIRE<br>WITH THIS VIDEO</div>
<div class="abs video-tools">
  <svg width="18" height="18" viewBox="0 0 24 24"><path fill="#fff" d="M12 21 3.5 12.6A5 5 0 0 1 12 6a5 5 0 0 1 8.5 6.6z"/></svg>
  <svg width="18" height="18" viewBox="0 0 24 24"><circle cx="12" cy="12" r="9" fill="none" stroke="#fff" stroke-width="2.5"/><path d="M12 7v5l3 2" stroke="#fff" stroke-width="2.5" fill="none"/></svg>
  <svg width="18" height="18" viewBox="0 0 24 24"><path fill="#fff" d="M2 11 22 3l-6 18-4-7z"/></svg>
</div>
<div class="abs video-bar">
  <svg width="16" height="16" viewBox="0 0 16 16"><path d="M3 2l11 6-11 6z" fill="#fff"/></svg>
  <div class="track"></div>
  <span class="hd">HD</span>
</div>

<section class="abs gallery">
  <h2>GALLERY</h2>
  <div class="gallery-rule"></div>
</section>
<div class="abs gallery-shadow"></div>
<div class="abs g-arrow" style="left:130px">&#10094;</div>
<div class="abs g-arrow" style="left:1044px">&#10095;</div>
<div class="abs thumb thumb-1" role="img" aria-label="Champagne bottle bursting open with sparkling spray"></div>
<div class="abs thumb thumb-2" role="img" aria-label="Hands raising champagne flutes in a toast"></div>
<div class="abs thumb thumb-3" role="img" aria-label="Plate of fresh red cherries on a checkered cloth"></div>

<footer class="abs footer">
  <div class="fcol about">
    <h3>ABOUT US</h3>
    <p>Lorem ipsum dolor sit amet, consectetuer adipis cing elit. Aenean commodo ligula eget dolor. Lorem ipsum dolor sit amet, consectetuer adipiscing elit. Aenean commodo ligula eget dolor. Aenean massa. Cum sociis natoque penatibus et magnis dis parturient montes, nascetur ridiculus mus. Donec quam felis, ultricies nec, pellentesque eu, pretium quis, sem.</p>
  </div>
  <div class="fcol address">
    <h3>ADDRESS</h3>
    <p>The Company Name Inc.<br>4120 - 4126 Alder Lane,<br>Brookfield, BK12 4RT</p>
    <p style="margin-top:18px">Freephone: &nbsp;+1 800 555 0147<br>Telephone: &nbsp;+1 800 555 0193<br>FAX: &nbsp;&nbsp;&nbsp;&nbsp;&nbsp;&nbsp;&nbsp;&nbsp;&nbsp;+1 800 555 0162<br>E-mail: <a>hello@velmorhaven.example</a></p>
  </div>
  <div class="fcol quotes">
    <h3>TESTIMONIALS</h3>
    <div class="quote">
      <div class="avatar" role="img" aria-label="Portrait of a guest"></div>
      <p>" Lorem ipsum dolor sit amet, consectetuer adipis cing elit. Aenean commodo ligula eget dolor. Lorem ipsum dolor sit amet, consectetuer adipiscing elit. "...<em>- Nora Pell</em></p>
    </div>
    <div class="quote">
      <div class="avatar" role="img" aria-label="Portrait of a guest"></div>
      <p>" Consectetuer adipis cing elit. Aenean commodo ligula eget dolor. Lorem ipsum dolor sit amet, consectetuer adipiscing elit. " Ut viverra mauris justo, quis...<em>- Evan Hollis</em></p>
    </div>
  </div>
</footer>
<div class="abs copyright">Copyright 2017, Velmorhaven All rights reserved by Fernwick Studio.</div>

</body>
</html>
```